Book Cover Design Project

I have written a booK called "Build From Nothing:
a handbook for launching and steering a modest enterprise. It is aimed at the start up entrepreneur and seeks to give them everything they need to start up and run a small business. I am interested in a very simple cover that is contemporary in the look but clearly communicates the mission of the book. It should sell very well as there are no others like it, so the designer will get excellent exposure.
Updates

Reason: I an vacation in Europe until the 23rd of July. Would like a few days to make a decision after my return Ned

We are currently on vacation.  Will make a final decision in about a week.  Thanks so much for your submissions

Ned

Target Market(s)

Start up businesses in the U.S.

Industry/Entity Type

Business

Requirements
Must have
• Clear communication of the name. Lots of white space. Graphic communication of the purpose of the book? Prominent exposure of my name. Edward r. Kistlewood

```html
<!DOCTYPE html>
<html lang="en">
<head>
<meta charset="utf-8">
<title>Build From Nothing – Book Cover</title>
<link rel="stylesheet" href="https://fonts.googleapis.com/css2?family=Bebas+Neue&display=swap">
<style>
  :root {
    --backdrop: #1b1b1b;
    --cover-white: #ffffff;
    --band-green: #6bb543;
    --ink: #0a0a0a;
    --art-top: #d9ead0;
    --art-bottom: #d39a6e;
  }
  * { box-sizing: border-box; margin: 0; padding: 0; }
  html, body {
    width: 1200px;
    height: 900px;
    overflow: hidden;
    background: var(--backdrop);
  }
  .canvas {
    position: relative;
    width: 1200px;
    height: 900px;
  }
  .book-cover {
    position: absolute;
    left: 368px;
    top: 88px;
    width: 464px;
    height: 722px;
    background: var(--cover-white);
    display: flex;
    flex-direction: column;
    align-items: center;
    font-family: 'Bebas Neue', sans-serif;
    color: var(--ink);
  }
  .author-band {
    width: 100%;
    height: 40px;
    background: var(--band-green);
    color: var(--cover-white);
    font-size: 28px;
    letter-spacing: 4px;
    line-height: 42px;
    text-align: center;
  }
  .book-title {
    margin-top: 14px;
    font-size: 102px;
    line-height: 0.88;
    font-weight: 400;
    text-align: center;
    letter-spacing: 1px;
  }
  .cover-art {
    display: block;
    margin-top: 20px;
    width: 250px;
    height: 160px;
  }
  .book-subtitle {
    margin-top: 28px;
    font-size: 53px;
    line-height: 0.96;
    font-weight: 400;
    text-align: center;
  }
</style>
</head>
<body>
  <main class="canvas">
    <article class="book-cover">
      <div class="author-band">Author Name</div>
      <h1 class="book-title">Build<br>From<br>Nothing:</h1>
      <svg class="cover-art" role="img" aria-label="Photograph of a green seedling sprouting from a pile of copper coins" viewBox="0 0 250 160">
        <defs>
          <linearGradient id="art-fill" x1="0" y1="0" x2="0" y2="1">
            <stop offset="0%" stop-color="var(--art-top)"/>
            <stop offset="100%" stop-color="var(--art-bottom)"/>
          </linearGradient>
        </defs>
        <rect x="0" y="0" width="250" height="160" fill="url(#art-fill)"/>
      </svg>
      <h2 class="book-subtitle">A Handbook for<br>Launching and Steering<br>a Modest Enterprise</h2>
    </article>
  </main>
</body>
</html>
```